Online eyewear company needs a couple Sign-In and Product Review page designs

We sell prescription glasses starting at $99 with Free Shipping. We have over 300 different styles and colors.Our website is under construction and we need an amazing Sign-In and Product Review Pages to help finish things off. Our brand is called VESKA and our website is called VESKAEYEWEAR.COM.

We need 5 simple sign-in and product review pages to help finish our website. Sample pages attached

We need the pages to go in order

Quick Checkout review
Sign-In
Prescription
Shipping & Payment
Final Review

Target Market(s)

20-50 that wears glasses

Industry/Entity Type

Eyewear

Colors
ffffff
919191
eaeaea
d3d3d3
dddddd
b7b7b7
000000
3176b5

Requirements
Must have
• Simple, creative, original. Must not be exactly like the photos attached. They're just templete of our casual, simple style.
• We need the pages to go in order
• Quick Checkout review
• Sign-In
• Prescription
• Shipping & Payment
• Final Review
Should not have
• Must not look exactly like the photos attached.

```html
<!DOCTYPE html>
<html lang="en">
<head>
<meta charset="utf-8">
<title>VESKA — Shipping &amp; Payment</title>
<link rel="stylesheet" href="https://fonts.googleapis.com/css2?family=Oswald:wght@500;600&family=Poppins:wght@400;500;600&display=swap">
<style>
  :root{
    --blue:#3176b5;
    --white:#ffffff;
    --ink:#000000;
    --text:#333333;
    --grey:#919191;
    --light:#eaeaea;
    --line:#dddddd;
    --soft:#d3d3d3;
    --mid:#b7b7b7;
    --accent:#d6007e;
  }
  *{box-sizing:border-box;margin:0;padding:0}
  html,body{width:1200px;height:1029px;overflow:hidden;background:var(--white)}
  body{font-family:'Poppins',sans-serif;color:var(--text);position:relative}
  .abs{position:absolute}

  .promo-bar{left:0;top:0;width:1200px;height:33px;background:var(--light);border-top:1px solid var(--mid);
    font-size:9.5px;text-align:center;line-height:33px;color:var(--ink)}
  .site-header{left:0;top:33px;width:1200px;height:52px;background:var(--white)}
  .brand{left:116px;top:10px;font-family:'Poppins',sans-serif;font-weight:400;font-size:21px;letter-spacing:4px;color:var(--ink)}
  .main-nav{left:296px;top:19px;display:flex;gap:18px;font-size:11.5px;font-weight:500;color:#444}
  .util-nav{left:938px;top:21px;display:flex;align-items:center;gap:8px;font-size:10.5px;color:#555}
  .util-nav .sep{color:var(--blue)}
  .util-nav .sign-in{margin-left:10px}
  .cart{left:1132px;top:14px;width:34px;height:34px;background:var(--white);border-radius:5px;
    box-shadow:0 1px 4px rgba(0,0,0,.3);display:flex;align-items:center;justify-content:center}
  .cart-badge{left:1124px;top:6px;width:16px;height:16px;border-radius:50%;background:var(--accent);color:var(--white);
    font-size:8px;text-align:center;line-height:16px}

  .hero{left:0;top:85px;width:1200px;height:301px;
    background:radial-gradient(ellipse at 50% 45%, #3a7fbd 0%, #3176b5 55%, #2e70ad 100%)}
  .hero-title{left:0;top:212px;width:1200px;text-align:center;font-family:'Oswald',sans-serif;font-weight:600;
    font-size:32px;color:var(--white)}

  .steps{left:395px;top:418px;width:411px;height:36px;background:var(--light);display:flex;font-size:11.5px;border-radius:2px}
  .step{display:flex;align-items:center;justify-content:center;color:#333}
  .step.prescription{width:140px}
  .step.current{width:148px;background:var(--blue);color:var(--white);font-weight:600}
  .step.review{flex:1}

  .section-title{left:250px;top:488px;font-family:'Oswald',sans-serif;font-weight:500;font-size:20px;color:#333}

  .panel{background:var(--white);box-shadow:0 0 8px rgba(0,0,0,.08)}
  .address-card{left:250px;top:527px;width:701px;height:95px}
  .address-name{left:28px;top:23px;font-family:'Oswald',sans-serif;font-weight:500;font-size:19px;color:var(--blue)}
  .address-note{left:28px;top:52px;font-size:14px;color:#333}
  .next-btn{left:651px;top:31px;width:34px;height:34px;background:var(--blue);border-radius:2px;
    box-shadow:0 3px 6px rgba(0,0,0,.25);display:flex;align-items:center;justify-content:center}

  .option{display:flex;align-items:center;gap:14px;font-size:14px;color:#333}
  .radio{width:15px;height:15px;border:1px solid var(--line);border-radius:3px;background:var(--white);
    display:flex;align-items:center;justify-content:center}
  .radio::after{content:"";width:9px;height:9px;background:var(--blue);border-radius:2px}
  .opt-existing{left:252px;top:651px}

  .card-panel{left:250px;top:696px;width:701px;height:95px}
  .card-brand{left:34px;top:34px;font-size:20px;font-weight:600;letter-spacing:1px;color:#1f2a6b}
  .card-lines{left:155px;top:20px;font-size:14px;line-height:31px;color:#333}

  .opt-new{left:252px;top:819px}
  .opt-install{left:543px;top:819px;align-items:flex-start}
  .opt-install .radio{margin-top:2px}
  .install-sub{display:block;font-size:10.5px;margin-top:4px}
  .learn-btn{left:821px;top:815px;width:85px;height:38px;background:var(--blue);color:var(--white);
    font-size:9.5px;font-weight:600;display:flex;align-items:center;justify-content:center;border-radius:2px}

  .summary{left:250px;top:879px;width:702px;height:119px;background:var(--blue);color:var(--white)}
  .summary-row{position:absolute;left:18px;right:24px;display:flex;justify-content:space-between;font-size:12px}
  .summary-row.sub{top:16px}
  .summary-row.ship{top:44px}
  .summary-row.ship span:last-child{margin-right:24px}
  .summary-rule{position:absolute;left:16px;right:18px;top:75px;height:1px;background:rgba(255,255,255,.5)}
  .summary-row.total{top:88px;font-weight:600}
</style>
</head>
<body>
  <div class="abs promo-bar">FREE SHIPPING IN CONTINENTAL US</div>

  <header class="abs site-header">
    <div class="abs brand">VESKA</div>
    <nav class="abs main-nav"><span>EYEGLASSES</span><span>ORDER LENSES</span></nav>
    <nav class="abs util-nav">
      <svg width="12" height="12" viewBox="0 0 12 12"><circle cx="5" cy="5" r="3.8" fill="none" stroke="#aaa" stroke-width="1.6"/><line x1="7.8" y1="7.8" x2="11" y2="11" stroke="#aaa" stroke-width="1.8"/></svg>
      <span>SEARCH</span><span class="sep">|</span><span>HELP</span><span class="sign-in">SIGN IN</span>
    </nav>
  </header>
  <div class="abs cart">
    <svg width="18" height="15" viewBox="0 0 18 15"><path d="M5 6 L9 1 L13 6" fill="none" stroke="#111" stroke-width="1.6"/><path d="M1 6 H17 L15 14 H3 Z" fill="#111"/></svg>
  </div>
  <div class="abs cart-badge">0</div>

  <section class="abs hero" role="img" aria-label="Faded photo of eyeglass frames on a blue background"></section>
  <h1 class="abs hero-title">SHIPPING &amp; PAYMENT</h1>

  <div class="abs steps">
    <div class="step prescription">PRESCRIPTION</div>
    <div class="step current">SHIPPING &amp; PAYMENT</div>
    <div class="step review">REVIEW</div>
  </div>

  <h2 class="abs section-title">CHOOSE A SHIPPING ADDRESS :</h2>

  <div class="abs panel address-card">
    <div class="abs address-name">MARLA QUINBY</div>
    <div class="abs address-note">this is the quickest option!</div>
    <div class="abs next-btn">
      <svg width="12" height="14" viewBox="0 0 12 14"><path d="M3 1 L9 7 L3 13" fill="none" stroke="#fff" stroke-width="2"/></svg>
    </div>
  </div>

  <label class="abs option opt-existing"><span class="radio"></span>Use Existing</label>

  <div class="abs panel card-panel">
    <div class="abs card-brand">CARDWAY</div>
    <div class="abs card-lines">Ending in 4673<br>Expires 50/22</div>
  </div>

  <label class="abs option opt-new"><span class="radio"></span>Add a&nbsp; New Credit Card</label>
  <label class="abs option opt-install"><span class="radio"></span><span>Pay with<span class="install-sub">3 Interest free payment of $65/month</span></span></label>
  <div class="abs learn-btn">LEARN MORE</div>

  <section class="abs summary">
    <div class="summary-row sub"><span>SUBTOTAL (2 ITEMS)</span><span>$195.00</span></div>
    <div class="summary-row ship"><span>SHIPPING</span><span>FREE</span></div>
    <div class="summary-rule"></div>
    <div class="summary-row total"><span>TOTAL</span><span>$195.00</span></div>
  </section>
</body>
</html>
```